Software engineering company needs business card

I need a cool business card. Company: Soft Belan Brindlewood Ave 41 58207 Sincity Name: Gerald Vanholt CEO / Managing Director & Owner

```html
<!DOCTYPE html>
<html lang="en">
<head>
<meta charset="utf-8">
<title>Soft Belan – Business Card</title>
<link href="https://fonts.googleapis.com/css2?family=Open+Sans:wght@400;600;700&display=swap" rel="stylesheet">
<style>
  :root {
    --page: #ececea;
    --green: #8dc63f;
    --green-light: #a3d45a;
    --graphite: #58595b;
    --ink: #1e1e1e;
    --white: #ffffff;
  }
  * { margin: 0; padding: 0; box-sizing: border-box; }
  html, body {
    width: 1200px; height: 1000px; overflow: hidden;
    background: var(--page);
    font-family: "Open Sans", Arial, sans-serif;
  }
  .canvas { position: relative; width: 1200px; height: 1000px; }

  .card {
    position: absolute;
    border-radius: 22px;
    overflow: hidden;
    box-shadow: 0 8px 18px rgba(0,0,0,.22);
  }
  .card-front {
    left: 160px; top: 200px; width: 560px; height: 310px;
    background: var(--green);
  }
  .front-pattern {
    position: absolute; left: 0; top: 0; width: 200px; height: 310px;
  }
  .front-wordmark {
    position: absolute; left: 240px; top: 128px;
    font-size: 40px; font-weight: 700; color: var(--graphite);
    letter-spacing: 1px;
  }

  .card-back {
    left: 486px; top: 505px; width: 520px; height: 300px;
    background: var(--green);
  }
  .back-bg { position: absolute; inset: 0; }
  .back-wordmark {
    position: absolute; left: 8px; top: 150px;
    transform: rotate(-53deg); transform-origin: left top;
    font-size: 30px; font-weight: 700; color: var(--graphite);
    letter-spacing: 4px; white-space: nowrap;
  }
  .contact {
    position: absolute; right: 32px; top: 122px;
    text-align: right; color: var(--ink);
  }
  .contact-name { font-size: 21px; font-weight: 700; line-height: 1.1; }
  .contact-name .first { color: var(--white); }
  .contact-role { font-size: 14px; margin-top: 3px; }
  .contact-lines { font-size: 13px; line-height: 1.32; margin-top: 14px; }
  .contact-address { font-size: 13px; line-height: 1.32; margin-top: 10px; color: var(--white); }
</style>
</head>
<body>
<div class="canvas">

  <section class="card card-front">
    <svg class="front-pattern" viewBox="0 0 200 310" role="img" aria-label="Decorative pattern of white rounded diagonal stripes and dots">
      <polygon points="0,40 190,0 200,0 40,310 0,310" fill="#e9f4d9"/>
    </svg>
    <div class="front-wordmark">Soft Belan</div>
  </section>

  <section class="card card-back">
    <svg class="back-bg" viewBox="0 0 520 300" preserveAspectRatio="none" aria-hidden="true">
      <polygon points="300,0 520,0 520,120" fill="var(--green-light)" opacity=".55"/>
      <polygon points="0,0 283,0 58,300 0,300" fill="var(--white)"/>
      <polygon points="283,0 294,0 70,300 58,300" fill="var(--graphite)"/>
      <polygon points="294,0 312,0 88,300 70,300" fill="var(--green-light)" opacity=".6"/>
    </svg>
    <div class="back-wordmark">Soft Belan</div>
    <div class="contact">
      <div class="contact-name"><span class="first">Gerald</span> Vanholt</div>
      <div class="contact-role">CEO / Geschäftsführer &amp; Inhaber</div>
      <div class="contact-lines">
        +12 456 987 3150<br>
        youremail@domain.com<br>
        www.yourwebsite.com
      </div>
      <div class="contact-address">
        Soft Belan, Brindlewood Ave 41<br>
        58207 Sincity
      </div>
    </div>
  </section>

</div>
</body>
</html>
```